Label Design for a New Alcoholized Root Beer

Create a design for a new alcoholized root beer. This is a new product category in the USA growing very rapidly. Root Beer is a popular flavor of Cola, but recently, beer manufacturers have added alcohol to it and have created a new product that has gained traction on the market at a tremendous rate.

Root Beer is vintage product that has been around for a hundred years. Consumers of this product are mostly male between the age of 30 to 45. They purchase this product for its nostalgia and vintage look and taste.

This product will be in a standard 355 mL brown bottle.

It is 5.9% abv.

The name of the product is ''Corvel's Hard Root Beer''.

We have uploaded some pictures of traditional root beers to give you an idea of the feel we want our product to have and also, the bottle the product will be filled in.

Target Market(s)

Consumers are male 30-45, same market as craft beer consumers

Industry/Entity Type

Product

Requirements
Must have
• Design must have a vintage feel to it

```html
<!DOCTYPE html>
<html lang="en">
<head>
<meta charset="utf-8">
<title>Corvel's Hard Root Beer – Label</title>
<link rel="stylesheet" href="https://fonts.googleapis.com/css2?family=Montserrat:wght@700;800&display=swap">
<style>
  :root {
    --backdrop: #3a6088;
    --label-white: #ececec;
    --label-red-dark: #6e0616;
    --label-red: #9c0a22;
    --label-red-bright: #c0002b;
    --letter-fill: #a20c26;
    --brand-maroon: #8a0a22;
    --text-white: #ffffff;
  }
  html, body {
    margin: 0;
    padding: 0;
    overflow: hidden;
  }
  .canvas {
    position: relative;
    width: 800px;
    height: 1200px;
    background: var(--backdrop);
    overflow: hidden;
    font-family: "Montserrat", Arial, sans-serif;
  }
  .label-art {
    position: absolute;
    inset: 0;
    width: 800px;
    height: 1200px;
  }
  .neck-name {
    font-family: "Montserrat", Arial, sans-serif;
    font-weight: 800;
    font-size: 15px;
    fill: var(--brand-maroon);
  }
  .brand-name {
    font-family: "Montserrat", Arial, sans-serif;
    font-weight: 800;
    font-size: 44px;
    fill: var(--brand-maroon);
  }
  .product-line {
    font-family: "Montserrat", Arial, sans-serif;
    font-weight: 800;
    font-size: 27px;
    fill: var(--text-white);
    letter-spacing: 0.5px;
  }
  .product-type {
    font-family: "Montserrat", Arial, sans-serif;
    font-weight: 700;
    font-size: 66px;
    fill: var(--letter-fill);
    stroke: var(--text-white);
    stroke-width: 5px;
    stroke-linejoin: round;
    paint-order: stroke fill;
    letter-spacing: 1px;
  }
</style>
</head>
<body>
<main class="canvas">
  <svg class="label-art" viewBox="0 0 800 1200" xmlns="http://www.w3.org/2000/svg" aria-labelledby="label-title">
    <title id="label-title">Corvel's Hard Root Beer</title>
    <defs>
      <linearGradient id="red-fill" x1="0" y1="0" x2="0" y2="1">
        <stop offset="0" stop-color="var(--label-red-dark)"/>
        <stop offset="0.55" stop-color="var(--label-red)"/>
        <stop offset="1" stop-color="var(--label-red-bright)"/>
      </linearGradient>
      <clipPath id="neck-shape">
        <polygon points="400,230 442,253 442,331 400,355 358,331 358,253"/>
      </clipPath>
    </defs>

    <g class="neck-label" clip-path="url(#neck-shape)">
      <rect x="350" y="225" width="100" height="135" fill="url(#red-fill)"/>
      <polygon points="350,225 450,225 450,292 350,310" fill="var(--label-white)"/>
    </g>
    <text class="neck-name" x="400" y="278" text-anchor="middle">Corvel's</text>

    <g class="body-label">
      <polygon points="292,745 515,705 515,905 400,953 292,905" fill="url(#red-fill)"/>
      <polygon points="292,688 515,648 515,705 292,745" fill="var(--label-white)"/>
      <text class="brand-name" x="403" y="712" text-anchor="middle" transform="rotate(-10 403 712)">Corvel's</text>
      <text class="product-line" x="403" y="804" text-anchor="middle">HARD ROOT</text>
      <text class="product-type" x="403" y="886" text-anchor="middle">BEER</text>
    </g>
  </svg>
</main>
</body>
</html>
```